Design 6 app screenshot for Vendora Shelf

I need 6 app screenshots(see example) for Vendora Shelf with text for my store listing (not app redesign).
You can download the screenshots directly from Vendora Shelf.

It is real simple task so you can show the first screen as example.

Link to Vendora Shelf:

Example:

Text:(order starts from left to right in Vendora Shelf link)
Image 1: Browse pets based on your location
Image 2: Map view
Image 3: Contact pet publisher
Image 4: No text
Image 5: No text
Image 6: Browse adopted pets

```html
<!DOCTYPE html>
<html lang="en">
<head>
<meta charset="utf-8">
<title>Vendora Shelf – Browse pets</title>
<link href="https://fonts.googleapis.com/css2?family=Mulish:ital,wght@0,400;0,500;0,700;1,400&family=Roboto:ital,wght@0,400;1,400&display=swap" rel="stylesheet">
<style>
  :root {
    --backdrop: #b1e998;
    --phone: #272727;
    --phone-shadow: #8fc07a;
    --phone-detail: #1c1c1c;
    --status-green: #2f8a1f;
    --bar-green: #b3e89a;
    --soft-green: #a6df88;
    --accent-green: #4cc22b;
    --card: #ffffff;
    --divider: #e3e3e3;
    --ink: #3d3d3d;
    --ink-soft: #6e6e6e;
  }
  * { box-sizing: border-box; margin: 0; padding: 0; }
  html, body { width: 667px; height: 1200px; overflow: hidden; background: var(--backdrop); }
  body { font-family: "Mulish", sans-serif; color: var(--ink); position: relative; }

  .phone-shadow { position: absolute; left: 59px; top: 103px; width: 513px; height: 1053px; border-radius: 86px; background: var(--phone-shadow); }
  .phone-body { position: absolute; left: 77px; top: 73px; width: 513px; height: 1053px; border-radius: 86px; background: var(--phone); }
  .phone-key { position: absolute; width: 6px; background: var(--phone); border-radius: 2px; }
  .phone-key.shade { background: var(--phone-shadow); }
  .camera { position: absolute; left: 329px; top: 105px; width: 8px; height: 8px; border-radius: 50%; background: var(--phone-detail); }
  .sensor { position: absolute; left: 244px; top: 133px; width: 16px; height: 16px; border-radius: 50%; background: var(--phone-detail); }
  .speaker { position: absolute; left: 289px; top: 138px; width: 89px; height: 7px; border-radius: 4px; background: var(--phone-detail); }
  .home-button { position: absolute; left: 292px; top: 1016px; width: 82px; height: 82px; border-radius: 50%; background: var(--phone-detail); }

  .screen {
    position: absolute; left: 108px; top: 200px; width: 608px; height: 1080px;
    transform: scale(0.7411); transform-origin: 0 0; overflow: hidden;
    background: linear-gradient(to bottom, var(--bar-green) 123px, #e6f8dc 330px, #ffffff 430px);
  }

  .status-bar {
    position: absolute; top: 0; left: 0; width: 608px; height: 44px;
    background: var(--status-green); color: #fff;
    display: flex; align-items: center; justify-content: space-between; padding: 0 12px 0 22px;
    font-family: "Roboto", sans-serif; font-size: 26px;
  }
  .status-left, .status-right { display: flex; align-items: center; gap: 10px; }
  .status-battery-text { font-size: 21px; }

  .app-bar {
    position: absolute; top: 44px; left: 0; width: 608px; height: 79px;
    background: var(--bar-green);
    display: flex; align-items: center; justify-content: space-between; padding: 0 24px 0 32px;
    box-shadow: 0 2px 4px rgba(0,0,0,0.12); z-index: 2;
  }

  .new-strip {
    position: absolute; top: 123px; left: 27px; width: 554px; height: 175px;
    background: var(--card); border-bottom: 2px solid #c9eeb8;
  }
  .new-pet { position: absolute; top: 30px; width: 84px; text-align: center; }
  .new-pet .thumb { width: 84px; height: 84px; border-radius: 50%; border: 2px solid #555; }
  .new-pet .label { margin-top: 10px; font-size: 20px; color: var(--soft-green); }

  .pet-list { position: absolute; top: 298px; left: 27px; width: 554px; }
  .pet-card { position: relative; height: 236px; background: var(--card); border-bottom: 2px solid var(--divider); }
  .pet-photo { position: absolute; left: 27px; top: 29px; width: 166px; height: 166px; border-radius: 50%; }
  .pet-name { position: absolute; left: 227px; top: 26px; font-size: 34px; font-weight: 500; line-height: 1; color: var(--ink); }
  .pet-name.bold { font-weight: 700; }
  .pet-species { position: absolute; left: 227px; top: 78px; font-size: 24px; line-height: 1; color: var(--ink-soft); }
  .pet-breed { position: absolute; left: 227px; top: 114px; font-size: 22px; line-height: 1; font-style: italic; color: var(--ink-soft); font-family: "Roboto", sans-serif; }
  .pet-distance {
    position: absolute; right: 30px; top: 180px; display: flex; align-items: center; gap: 8px;
    font-size: 20px; line-height: 1; font-style: italic; color: var(--soft-green);
  }

  .search-dock { position: absolute; left: 0; top: 1002px; width: 608px; height: 78px; background: #fff; }
  .search-bar {
    position: absolute; left: 14px; top: 1010px; width: 580px; height: 62px; border-radius: 31px;
    background: var(--bar-green); display: flex; align-items: center; padding-left: 38px;
  }
</style>
</head>
<body>
  <div class="phone-shadow"></div>
  <div class="phone-key shade" style="left:55px;top:237px;height:40px"></div>
  <div class="phone-key shade" style="left:55px;top:327px;height:76px"></div>
  <div class="phone-key shade" style="left:55px;top:423px;height:76px"></div>
  <div class="phone-key" style="left:72px;top:209px;height:40px"></div>
  <div class="phone-key" style="left:72px;top:299px;height:76px"></div>
  <div class="phone-key" style="left:72px;top:394px;height:77px"></div>
  <div class="phone-key" style="left:589px;top:299px;height:76px"></div>
  <div class="phone-body"></div>
  <div class="camera"></div>
  <div class="sensor"></div>
  <div class="speaker"></div>
  <div class="home-button"></div>

  <div class="screen">
    <header class="status-bar">
      <div class="status-left">
        <svg width="16" height="26" viewBox="0 0 18 28" fill="#fff"><rect x="8" y="2" width="2" height="24"/><circle cx="9" cy="25" r="3"/><rect x="2" y="8" width="2" height="6"/><rect x="14" y="6" width="2" height="6"/><rect x="2" y="13" width="7" height="2"/><rect x="9" y="11" width="7" height="2"/></svg>
        <span style="width:10px"></span>
        <svg width="26" height="24" viewBox="0 0 28 26" fill="#fff"><ellipse cx="14" cy="15" rx="9" ry="10"/><rect x="0" y="12" width="5" height="2"/><rect x="23" y="12" width="5" height="2"/><rect x="0" y="19" width="5" height="2"/><rect x="23" y="19" width="5" height="2"/><rect x="7" y="1" width="2" height="5"/><rect x="19" y="1" width="2" height="5"/></svg>
      </div>
      <div class="status-right">
        <svg width="24" height="32" viewBox="0 0 26 34" fill="none" stroke="#fff" stroke-width="3"><rect x="6" y="3" width="16" height="28" rx="2"/><line x1="2" y1="8" x2="2" y2="16"/></svg>
        <svg width="32" height="32" viewBox="0 0 34 34" fill="none" stroke="#fff" stroke-width="3"><circle cx="17" cy="19" r="12"/><polyline points="17,12 17,19 22,22"/><line x1="3" y1="7" x2="8" y2="3"/><line x1="31" y1="7" x2="26" y2="3"/></svg>
        <svg width="34" height="26" viewBox="0 0 36 28" fill="none" stroke="#fff" stroke-width="3.5" stroke-linecap="round"><path d="M3 10a22 22 0 0 1 30 0"/><path d="M8 16a14 14 0 0 1 20 0"/><path d="M13 21a7 7 0 0 1 10 0"/><circle cx="18" cy="25" r="1.5" fill="#fff"/></svg>
        <svg width="32" height="30" viewBox="0 0 34 32" fill="#fff"><rect x="1" y="22" width="5" height="10"/><rect x="9" y="16" width="5" height="16"/><rect x="17" y="10" width="5" height="22"/><rect x="25" y="2" width="5" height="30" opacity=".6"/></svg>
        <span class="status-battery-text">58%</span>
        <svg width="18" height="30" viewBox="0 0 20 32"><rect x="1" y="3" width="18" height="28" fill="none" stroke="#fff" stroke-width="2"/><rect x="6" y="0" width="8" height="3" fill="#fff"/><rect x="1" y="15" width="18" height="16" fill="#fff"/></svg>
        <span>21:48</span>
      </div>
    </header>

    <nav class="app-bar">
      <svg width="32" height="24" viewBox="0 0 36 26" fill="#fff"><rect y="0" width="36" height="3.5"/><rect y="11" width="36" height="3.5"/><rect y="22" width="36" height="3.5"/></svg>
      <svg width="31" height="33" viewBox="0 0 34 36" fill="#fff"><path d="M0 5 L11 0 L23 5 L34 0 V31 L23 36 L11 31 L0 36 Z M12 4 V30 L22 34 V8 Z" fill-rule="evenodd"/></svg>
    </nav>

    <section class="new-strip">
      <div class="new-pet" style="left:14px"><div class="thumb" role="img" aria-label="Photo of a newly listed dark pet" style="background:radial-gradient(circle,#4a3a2c,#1c1915)"></div><div class="label">New</div></div>
      <div class="new-pet" style="left:125px"><div class="thumb" role="img" aria-label="Photo of a newly listed husky puppy" style="background:radial-gradient(circle,#d8d8dc,#2a2a2e)"></div><div class="label">New</div></div>
      <div class="new-pet" style="left:236px"><div class="thumb" role="img" aria-label="Photo of a newly listed golden dog" style="background:radial-gradient(circle,#d9a66a,#8d5e33)"></div><div class="label">New</div></div>
      <div class="new-pet" style="left:348px"><div class="thumb" role="img" aria-label="Photo of a newly listed black kitten" style="background:radial-gradient(circle,#3a3a3a,#e8e6e2)"></div><div class="label">New</div></div>
      <div class="new-pet" style="left:459px"><div class="thumb" role="img" aria-label="Photo of a newly listed white pet lying down" style="background:radial-gradient(circle,#e9e1d6,#5c4331)"></div><div class="label">New</div></div>
    </section>

    <section class="pet-list">
      <article class="pet-card">
        <div class="pet-photo" role="img" aria-label="Photo of Emma, a Scottish fold cat on a blanket" style="background:radial-gradient(circle at 55% 50%,#a89a88,#c9d3e2 70%)"></div>
        <h2 class="pet-name bold">эмма</h2>
        <p class="pet-species">Cat</p>
        <p class="pet-breed">шотландская вислоухая</p>
        <p class="pet-distance">1365 km <svg width="20" height="20" viewBox="0 0 22 22" fill="var(--accent-green)"><path d="M21 1 L1 9 L10 12 L13 21 Z"/></svg></p>
      </article>
      <article class="pet-card">
        <div class="pet-photo" role="img" aria-label="Photo of Tomas, a Siberian cat lying on a cushion" style="background:radial-gradient(circle at 50% 55%,#e6e2de,#b08a70 75%)"></div>
        <h2 class="pet-name">Tomas</h2>
        <p class="pet-species">Cat</p>
        <p class="pet-breed">сибирский</p>
        <p class="pet-distance">1751 km <svg width="20" height="20" viewBox="0 0 22 22" fill="var(--accent-green)"><path d="M21 1 L1 9 L10 12 L13 21 Z"/></svg></p>
      </article>
      <article class="pet-card">
        <div class="pet-photo" role="img" aria-label="Photo of Bona, a Siberian calico kitten on a cushion" style="background:radial-gradient(circle at 55% 55%,#efe8e2,#b58a6c 75%)"></div>
        <h2 class="pet-name">Bona</h2>
        <p class="pet-species">Cat</p>
        <p class="pet-breed">сибирская</p>
        <p class="pet-distance">1751 km <svg width="20" height="20" viewBox="0 0 22 22" fill="var(--accent-green)"><path d="M21 1 L1 9 L10 12 L13 21 Z"/></svg></p>
      </article>
    </section>

    <div class="search-dock"></div>
    <div class="search-bar">
      <svg width="30" height="30" viewBox="0 0 34 34" fill="none" stroke="#fff" stroke-width="4" stroke-linecap="round"><circle cx="13" cy="13" r="10"/><line x1="21" y1="21" x2="31" y2="31"/></svg>
    </div>
  </div>
</body>
</html>
```